website for LanternPeak Advisory - a HR Consultancy Company

Creation of a website template. I would like to make it with with Wix, but am open to other online website programms.

Website is for consulting company in human resources offering the following services:
- Human resources and talent management for small companies
- Human resources consulting for start-ups
- Diversity and Inclusion management/training
- Board of Directors - talent identification and need evalutation
- coaching and counseling

Pages needed:
- Home page
- HR and talent management
- HR consulting for start-ups
- Diversity & Inclusion management/training
- coaching and counseling
- contact

1. My logo below
2. an example website that I like (not in terms of colours): https://www.mapleridgeadvisors.ch/
http://www.veldorquint.ch/

Target Market(s)

small and mid-sized companies, start-ups

Industry/Entity Type

Consulting

Number of Pages Required

5+ page

Font styles to use
Serif
Sans Serif

Colors
3277b5
35a7d7

Requirements
Must have
• - easy on the eye yet professional looking
• - my text is short
• - website should be clear and easy to understand
Nice to have
• - I will include photographs of the coaches
Should not have
• too many colours
• complicated

```html
<!DOCTYPE html>
<html lang="en">
<head>
<meta charset="utf-8">
<title>LanternPeak Advisory – HR Consulting</title>
<link href="https://fonts.googleapis.com/css2?family=Roboto:ital,wght@0,300;0,400;0,500;0,700;1,400&display=swap" rel="stylesheet">
<style>
:root{
  --blue:#3277b5;
  --sky:#35a7d7;
  --ink:#222;
  --text:#555;
  --muted:#888;
  --line:#e4e4e4;
  --soft:#f1f0f5;
  --dark:#2f2f2f;
  --darker:#1f1f1f;
  --white:#fff;
}
*{box-sizing:border-box;margin:0;padding:0}
html,body{width:1200px;height:3838px;overflow:hidden}
body{font-family:"Roboto",Arial,sans-serif;color:var(--text);background:var(--white);position:relative}
.abs{position:absolute}
section,header,footer,nav{position:absolute;left:0;width:1200px}

/* header */
.site-header{top:0;height:107px;border-top:6px solid var(--blue)}
.follow{left:66px;top:28px;font-size:14px;color:var(--ink)}
.follow-dots{left:66px;top:64px;display:flex;gap:9px}
.follow-dots span{width:11px;height:11px;border-radius:50%;background:#777}
.brand{left:0;width:1200px;top:30px;text-align:center;white-space:nowrap}
.brand-mark{display:inline-block;width:30px;height:30px;border-radius:50%;background:var(--blue);vertical-align:middle;margin-right:10px}
.brand-name{font-size:24px;font-weight:700;color:var(--blue);vertical-align:middle;letter-spacing:.5px}
.contact-top{left:1005px;top:30px;font-size:14px;color:var(--ink);line-height:34px;white-space:nowrap}
.contact-top svg{vertical-align:-2px;margin-right:8px}

.main-nav{top:107px;height:46px;border-top:1px solid var(--line)}
.main-nav a{position:absolute;top:14px;font-size:14px;color:var(--ink);text-decoration:none;white-space:nowrap}
.quote-btn{left:952px;top:0;width:122px;height:46px;background:var(--blue);color:var(--white);font-size:14px;font-weight:500;display:flex;align-items:center;justify-content:center;clip-path:polygon(12px 0,100% 0,100% 100%,0 100%)}
.search-btn{left:1074px;top:0;width:57px;height:46px;background:#e6e6e6;display:flex;align-items:center;justify-content:center}

/* hero */
.hero{top:153px;height:581px;overflow:hidden}
.hero-photo{position:absolute;inset:0;background:
  radial-gradient(ellipse 300px 260px at 860px 210px,rgba(190,150,120,.55),rgba(0,0,0,0) 70%),
  radial-gradient(ellipse 420px 200px at 720px 560px,rgba(220,215,210,.45),rgba(0,0,0,0) 70%),
  radial-gradient(ellipse 260px 300px at 1080px 360px,rgba(40,38,40,.8),rgba(0,0,0,0) 70%),
  linear-gradient(90deg,#5a5f64 0%,#6c6f70 30%,#8a857c 55%,#4d4843 80%,#2e2b2a 100%)}
.hero-shade{position:absolute;inset:0;background:linear-gradient(90deg,rgba(0,0,0,.5),rgba(0,0,0,.1) 60%,rgba(0,0,0,0))}
.hero h1{left:66px;top:150px;font-size:64px;font-weight:700;color:var(--white);white-space:nowrap}
.hero p{left:66px;top:228px;width:640px;font-size:15px;line-height:20px;color:var(--white)}
.btn{background:var(--blue);color:var(--white);font-size:15px;font-weight:500;display:flex;align-items:center;justify-content:center;border-radius:2px}
.hero .btn{left:66px;top:293px;width:162px;height:51px}

/* intro */
.intro{top:734px;height:558px}
.intro-lead{top:36px;left:0;width:1200px;text-align:center;font-size:32px;font-weight:300;line-height:39px;color:#666}
.intro-lead em{font-style:normal;color:var(--sky)}
.service-card{top:192px;width:310px}
.service-photo{height:220px}
.service-card h3{position:absolute;top:245px;left:0;font-size:15px;font-weight:500;color:var(--ink);white-space:nowrap}
.service-card p{position:absolute;top:276px;left:0;font-size:15px;color:var(--text);white-space:nowrap}
.service-arrow{position:absolute;top:251px;left:271px;width:39px;height:43px;border:1px solid var(--line);display:flex;align-items:center;justify-content:center}

/* committed band */
.committed{top:1292px;height:486px;overflow:hidden}
.committed-photo{position:absolute;inset:0;background:
  radial-gradient(ellipse 260px 240px at 900px 190px,rgba(225,215,205,.7),rgba(0,0,0,0) 70%),
  radial-gradient(ellipse 300px 180px at 950px 430px,rgba(200,200,205,.6),rgba(0,0,0,0) 70%),
  linear-gradient(90deg,#2a5f86 0%,#3b7398 30%,#6e8aa0 55%,#a9b4bd 75%,#c8cdd2 100%)}
.committed h2{left:66px;top:130px;font-size:52px;font-weight:500;line-height:55px;color:var(--white);white-space:nowrap}
.play{left:66px;top:258px}
.committed p{left:151px;top:268px;font-size:15px;line-height:19px;color:var(--white)}

/* approach */
.approach{top:1778px;height:591px}
.section-title{left:0;width:1200px;text-align:center;font-size:33px;font-weight:500;color:var(--ink)}
.section-sub{left:0;width:1200px;text-align:center;font-size:15px;color:var(--text)}
.approach-card{top:140px;width:327px;height:379px;border:1px solid var(--line)}
.approach-photo{height:205px}
.approach-card h3{position:absolute;left:12px;top:222px;font-size:22px;font-weight:500;color:var(--ink);white-space:nowrap}
.approach-card p{position:absolute;left:12px;top:256px;width:300px;font-size:14px;line-height:19px;color:var(--text)}
.approach-card a{position:absolute;left:12px;top:332px;font-size:14px;font-weight:500;color:var(--ink);text-decoration:none}

/* testimonial */
.testimonial{top:2369px;height:432px;background:var(--soft)}
.testimonial-photo{left:0;top:0;width:558px;height:432px;background:
  radial-gradient(ellipse 170px 220px at 330px 250px,rgba(40,45,55,.75),rgba(0,0,0,0) 70%),
  linear-gradient(135deg,#4a4d50,#6c7073 55%,#8e9295)}
.avatars{left:609px;top:93px;display:flex;gap:9px}
.avatars span{width:44px;height:44px;border-radius:50%;background:#d4d4d8}
.avatars span:nth-child(2){background:#5a5a5e}
.testimonial blockquote{position:absolute;left:609px;top:163px;width:545px;font-size:14px;line-height:20px;color:var(--text)}
.testimonial .who{left:609px;top:296px;font-size:14px;font-weight:500;color:var(--ink)}
.testimonial .where{left:609px;top:320px;font-size:13px;color:var(--text)}

/* coaches */
.coaches{top:2801px;height:583px}
.coach-card{top:169px;width:241px;height:363px;border:1px solid #eee}
.coach-photo{height:266px;border-bottom:5px solid var(--sky)}
.coach-card h3{position:absolute;top:290px;left:0;width:100%;text-align:center;font-size:20px;font-weight:500;color:var(--ink);white-space:nowrap}
.coach-card p{position:absolute;top:322px;left:0;width:100%;text-align:center;font-size:13px;font-style:italic;color:var(--muted)}

/* call band */
.call-band{top:3384px;height:146px;background:var(--dark)}
.call-blue{left:0;top:0;width:550px;height:146px;background:var(--blue);clip-path:polygon(0 0,100% 0,94% 100%,0 100%)}
.call-band .call-note{left:274px;top:24px;font-size:17px;color:#9fd3ee;white-space:nowrap}
.call-band .call-number{left:218px;top:54px;font-size:39px;font-weight:700;color:var(--white);white-space:nowrap}
.quote-title{left:578px;top:36px;font-size:21px;font-weight:500;color:var(--white)}
.field{top:80px;width:202px;height:33px;background:#e4e4e4;font-size:13px;color:#777;padding:9px 8px}
.subscribe{left:1016px;top:80px;width:104px;height:33px;font-size:14px}

/* footer */
.site-footer{top:3530px;height:248px;background:var(--dark);color:#ddd}
.footer-title{top:42px;font-size:22px;font-weight:500;color:var(--white)}
.footer-links{top:92px;font-size:13px;line-height:23px;list-style:none}
.contact-row{font-size:13px;line-height:18px;color:#ddd;white-space:nowrap}
.icon-dot{position:absolute;width:26px;height:26px;border-radius:50%;background:#666;display:flex;align-items:center;justify-content:center}
.social{font-size:13px;color:#ddd;width:180px;height:28px}
.social span{position:absolute;left:0;top:0;width:28px;height:28px;border-radius:50%}
.social b{position:absolute;left:42px;top:6px;font-weight:500;letter-spacing:.5px;white-space:nowrap}
.footer-brand{left:880px;top:72px;width:250px;text-align:center}
.footer-brand .brand-mark{background:#9a9a9a;width:44px;height:44px;margin:0 0 10px}
.footer-brand div{font-size:19px;font-weight:700;color:#9a9a9a;white-space:nowrap}
.copyright{top:3778px;height:60px;background:var(--darker);color:#ddd;font-size:14px;text-align:center;line-height:60px}
</style>
</head>
<body>

<header class="site-header">
  <div class="abs follow">Follow Us :</div>
  <div class="abs follow-dots"><span></span><span></span><span></span><span></span><span></span></div>
  <div class="abs brand"><span class="brand-mark"></span><span class="brand-name">LanternPeak Advisory</span></div>
  <div class="abs contact-top">
    <div><svg width="14" height="14" viewBox="0 0 24 24"><path fill="#333" d="M6.6 10.8a15 15 0 0 0 6.6 6.6l2.2-2.2a1 1 0 0 1 1-.25 11.4 11.4 0 0 0 3.6.57 1 1 0 0 1 1 1V20a1 1 0 0 1-1 1A17 17 0 0 1 3 4a1 1 0 0 1 1-1h3.5a1 1 0 0 1 1 1c0 1.25.2 2.45.57 3.57a1 1 0 0 1-.25 1z"/></svg>(+41) 44 555 0182</div>
    <div><svg width="14" height="14" viewBox="0 0 24 24"><path fill="#333" d="M2 21l21-9L2 3v7l15 2-15 2z"/></svg>hello@lanternpeak.ch</div>
  </div>
</header>

<nav class="main-nav">
  <a style="left:84px">Home</a>
  <a style="left:159px">Hr Consulting</a>
  <a style="left:281px">Diversity &amp; Inclusion</a>
  <a style="left:450px">Board Of Directors</a>
  <a style="left:604px">Coaching And Counselling</a>
  <a style="left:806px">Contact</a>
  <div class="abs quote-btn">GET A QUOTE</div>
  <div class="abs search-btn"><svg width="20" height="20" viewBox="0 0 24 24"><circle cx="10" cy="10" r="6" fill="none" stroke="#444" stroke-width="2"/><path d="M14.5 14.5L20 20" stroke="#444" stroke-width="2.4"/></svg></div>
</nav>

<section class="hero">
  <div class="hero-photo" role="img" aria-label="Businessman in glasses talking on the phone at a desk with a laptop"></div>
  <div class="hero-shade"></div>
  <h1 class="abs">Grow Your Business</h1>
  <p class="abs">There are many variations of passages of Lorem Ipsum available, but the majority have suffered alteration in some form, by injected humour.</p>
  <div class="abs btn">GET STARTED</div>
</section>

<section class="intro">
  <p class="abs intro-lead"><em>Over 80 countries</em> our teams of research consultants<br>&amp; expert analyst conduct qualitative and quantitative<br>research in across the globe.</p>
  <div class="abs service-card" style="left:102px">
    <div class="service-photo" role="img" aria-label="Hands working over charts and a laptop" style="background:radial-gradient(ellipse 120px 90px at 200px 70px,rgba(255,250,240,.8),rgba(0,0,0,0) 70%),linear-gradient(135deg,#b58d66,#d8c4aa 45%,#efe7dc 70%,#8f7c68)"></div>
    <h3>Business Advisor</h3><p>Get financial advise wih expert</p>
    <div class="service-arrow"><svg width="10" height="14" viewBox="0 0 10 14"><path d="M2 1l6 6-6 6" fill="none" stroke="#bbb" stroke-width="1.6"/></svg></div>
  </div>
  <div class="abs service-card" style="left:440px">
    <div class="service-photo" role="img" aria-label="Two colleagues talking at a bright office table" style="background:radial-gradient(ellipse 90px 110px at 230px 110px,rgba(240,240,245,.9),rgba(0,0,0,0) 70%),linear-gradient(135deg,#c9a98c,#e8dccf 40%,#f4f1ec 65%,#9fb3c6)"></div>
    <h3>Floor Paving</h3><p>750+ experts to care your house</p>
    <div class="service-arrow"><svg width="10" height="14" viewBox="0 0 10 14"><path d="M2 1l6 6-6 6" fill="none" stroke="#bbb" stroke-width="1.6"/></svg></div>
  </div>
  <div class="abs service-card" style="left:778px">
    <div class="service-photo" role="img" aria-label="Team meeting around a table in a glass-walled office" style="background:radial-gradient(ellipse 150px 60px at 155px 190px,rgba(70,70,80,.5),rgba(0,0,0,0) 70%),linear-gradient(135deg,#c7d2da,#e9eef1 45%,#b5c2cc 75%,#7f8b96)"></div>
    <h3>Tiles Supplier</h3><p>Wide range of tiles collection</p>
    <div class="service-arrow"><svg width="10" height="14" viewBox="0 0 10 14"><path d="M2 1l6 6-6 6" fill="none" stroke="#bbb" stroke-width="1.6"/></svg></div>
  </div>
</section>

<section class="committed">
  <div class="committed-photo" role="img" aria-label="Woman in glasses working on a laptop, tinted blue"></div>
  <h2 class="abs">We Are Always<br>Committed</h2>
  <svg class="abs play" width="69" height="69" viewBox="0 0 69 69"><circle cx="34.5" cy="34.5" r="32" fill="none" stroke="#fff" stroke-width="4"/><path d="M27 21l22 13.5L27 48z" fill="#fff"/></svg>
  <p class="abs">Lorem ipsum dolor<br>sit amet con.</p>
</section>

<section class="approach">
  <h2 class="abs section-title" style="top:34px">Investment Approach</h2>
  <p class="abs section-sub" style="top:90px">Lorem ipsum dolor sit amet consectetur adipisicing elit sed do eiusm temp</p>
  <div class="abs approach-card" style="left:77px">
    <div class="approach-photo" role="img" aria-label="Group of colleagues smiling around a laptop" style="background:radial-gradient(ellipse 140px 80px at 160px 170px,rgba(90,100,120,.6),rgba(0,0,0,0) 70%),linear-gradient(135deg,#e3e8ec,#c9b7a4 45%,#8c98a4 75%,#5f6b76)"></div>
    <h3>Business Advisor</h3>
    <p>Lorem ipsum dolor sit amet, consectetur adipis elit sed do eiusmod tempor incidunt labore et dolore magna aliqua.</p>
    <a>Read More</a>
  </div>
  <div class="abs approach-card" style="left:435px">
    <div class="approach-photo" role="img" aria-label="Young team gathered around a tablet" style="background:radial-gradient(ellipse 110px 90px at 250px 110px,rgba(150,40,40,.45),rgba(0,0,0,0) 70%),linear-gradient(135deg,#a37e62,#dcc6b0 40%,#b48f74 70%,#6e5444)"></div>
    <h3>Investment Plan</h3>
    <p>Lorem ipsum dolor sit amet, consectetur adipis elit sed do eiusmod tempor incidunt labore et dolore magna aliqua.</p>
    <a>Read More</a>
  </div>
  <div class="abs approach-card" style="left:793px">
    <div class="approach-photo" role="img" aria-label="Woman working on a laptop in a bright room" style="background:radial-gradient(ellipse 90px 110px at 210px 110px,rgba(150,120,90,.55),rgba(0,0,0,0) 70%),linear-gradient(135deg,#d9dde0,#f5f3ef 45%,#d8cbbb 75%,#a8977f)"></div>
    <h3>Market Analyze</h3>
    <p>Lorem ipsum dolor sit amet, consectetur adipis elit sed do eiusmod tempor incidunt labore et dolore magna aliqua.</p>
    <a>Read More</a>
  </div>
</section>

<section class="testimonial">
  <div class="abs testimonial-photo" role="img" aria-label="Man sitting at a table looking at his phone"></div>
  <div class="abs avatars" role="img" aria-label="Client portrait thumbnails"><span></span><span></span><span></span></div>
  <blockquote>Lorem ipsum dolor sit amet consectetur adipiscing elit sed do eiusmod tempor incididunt labore dolore magna aliquaenim minim veniam quis nostrud exercitation ullamco laboris nisi ut aliquip ex ea commodo consequat duis aute irure dolor in rep rehenderit in voluptate velit esse cillum dolore eu fugiat nulla pariatur excepteur.</blockquote>
  <div class="abs who">Tobias Lindqvist</div>
  <div class="abs where">Newyork</div>
</section>

<section class="coaches">
  <h2 class="abs section-title" style="top:50px">Our Coaches</h2>
  <p class="abs section-sub" style="top:104px">Lorem ipsum dolor sit amet consectetur adipisicing elit sed do eiusm temp</p>
  <div class="abs coach-card" style="left:79px">
    <div class="coach-photo" role="img" aria-label="Portrait of a coach" style="background:radial-gradient(ellipse 90px 140px at 120px 190px,rgba(60,50,45,.55),rgba(0,0,0,0) 75%),linear-gradient(180deg,#f6f6f6,#e8e6e4)"></div>
    <h3>Clara Wenden</h3><p>Limo Advisor</p>
  </div>
  <div class="abs coach-card" style="left:345px">
    <div class="coach-photo" role="img" aria-label="Portrait of a coach" style="background:radial-gradient(ellipse 100px 140px at 120px 190px,rgba(170,140,100,.6),rgba(0,0,0,0) 75%),linear-gradient(180deg,#f6f6f6,#e8e6e4)"></div>
    <h3>Marco Reuss</h3><p>Limo Advisor</p>
  </div>
  <div class="abs coach-card" style="left:614px">
    <div class="coach-photo" role="img" aria-label="Portrait of a coach" style="background:radial-gradient(ellipse 95px 140px at 120px 190px,rgba(120,115,115,.55),rgba(0,0,0,0) 75%),linear-gradient(180deg,#f6f6f6,#e8e6e4)"></div>
    <h3>Elena Marsh</h3><p>Limo Advisor</p>
  </div>
  <div class="abs coach-card" style="left:880px">
    <div class="coach-photo" role="img" aria-label="Portrait of a coach" style="background:radial-gradient(ellipse 100px 140px at 120px 190px,rgba(210,210,215,.9),rgba(0,0,0,0) 75%),radial-gradient(ellipse 50px 50px at 120px 90px,rgba(150,120,100,.45),rgba(0,0,0,0) 75%),linear-gradient(180deg,#f6f6f6,#e4e4e4)"></div>
    <h3>Jonas Feller</h3><p>Limo Advisor</p>
  </div>
</section>

<section class="call-band">
  <div class="abs call-blue"></div>
  <div class="abs call-note">You can call us toll free</div>
  <div class="abs call-number">+(800) 555-0147</div>
  <div class="abs quote-title">Request a Free Quote</div>
  <div class="abs field" style="left:578px">Name</div>
  <div class="abs field" style="left:796px">Email</div>
  <div class="abs btn subscribe">Subscribe</div>
</section>

<footer class="site-footer">
  <h4 class="abs footer-title" style="left:77px">Quick Links</h4>
  <ul class="abs footer-links" style="left:77px"><li>Home</li><li>How it works</li><li>Features</li><li>Pricing</li><li>Contact us</li></ul>
  <ul class="abs footer-links" style="left:235px"><li>Terms of use</li><li>Reseller</li><li>Sitemap</li><li>Uptime Report</li></ul>

  <h4 class="abs footer-title" style="left:404px">Contact Us</h4>
  <div class="icon-dot" style="left:404px;top:88px"><svg width="12" height="14" viewBox="0 0 12 16"><path d="M6 0a6 6 0 0 1 6 6c0 4.5-6 10-6 10S0 10.5 0 6a6 6 0 0 1 6-6z" fill="#fff"/><circle cx="6" cy="6" r="2.2" fill="#666"/></svg></div>
  <div class="abs contact-row" style="left:443px;top:86px"><b>LANTERNPEAK ADVISORY</b><br>14 Birchwood Lane<br>Zurich 8004</div>
  <div class="icon-dot" style="left:404px;top:151px"><svg width="12" height="12" viewBox="0 0 24 24"><path fill="#fff" d="M6.6 10.8a15 15 0 0 0 6.6 6.6l2.2-2.2a1 1 0 0 1 1-.25 11.4 11.4 0 0 0 3.6.57 1 1 0 0 1 1 1V20a1 1 0 0 1-1 1A17 17 0 0 1 3 4a1 1 0 0 1 1-1h3.5a1 1 0 0 1 1 1c0 1.25.2 2.45.57 3.57a1 1 0 0 1-.25 1z"/></svg></div>
  <div class="abs contact-row" style="left:443px;top:155px">044-555-0193</div>
  <div class="icon-dot" style="left:404px;top:194px"><svg width="13" height="10" viewBox="0 0 13 10"><rect x=".5" y=".5" width="12" height="9" fill="none" stroke="#fff"/><path d="M.5.5l6 5 6-5" fill="none" stroke="#fff"/></svg></div>
  <div class="abs contact-row" style="left:443px;top:198px">info@lanternpeak.ch</div>

  <h4 class="abs footer-title" style="left:688px">Follow Us</h4>
  <div class="abs social" style="left:688px;top:88px"><span style="background:var(--blue)"></span><b>COMMUNITY</b></div>
  <div class="abs social" style="left:688px;top:133px"><span style="background:var(--sky)"></span><b>NEWS FEED</b></div>
  <div class="abs social" style="left:688px;top:180px"><span style="background:#d9552b"></span><b>UPDATES</b></div>

  <div class="abs footer-brand"><span class="brand-mark"></span><div>LanternPeak Advisory</div></div>
</footer>

<div class="abs copyright" style="left:0;width:1200px">LanternPeak Advisory | All rights reserved. Copyright 2016-2017</div>

</body>
</html>
```